Business card design for upmarket Home Technology design and Installation company

Hello designers, we need a great business card designed.
We need it to convey high tech, and also sophistication .
We work with some of the most affluent people in the world building them home technology systems, and A/V entertainment systems.

Services offered include the following:
Design, sales, installation, and maintenance of

*Home Automation systems
*Distributed / Multi-Room Audio and Video
*High Performance Networks & WiFi
* Lighting and Shade Control
*Home cinema
*Security and CCTV Systems

I have included a copy of our logo to use for your design efforts.

Target Market(s)

Upmarket clients with multi million euro villas.

Industry/Entity Type

Home technology

Contact Information for Business Card

NAME: Derek Halloran ADDRESS: Plaza Brisa Local 42, Port Andratx, 07392 PHONE: +34-602-518-794 EMAIL: DHalloran@VELTRAsmarthomes.com WEB: www.veltrasmarthomes.com

Requirements
Must have
• Our Logo, and our tagline

```html
<!DOCTYPE html>
<html lang="en">
<head>
<meta charset="utf-8">
<title>VELTRA Smarter Homes – Business Card</title>
<link href="https://fonts.googleapis.com/css2?family=Montserrat:wght@700&family=Open+Sans:wght@400;600&display=swap" rel="stylesheet">
<style>
  :root {
    --page: #efe9e1;
    --navy-deep: #111a33;
    --navy: #1a2d55;
    --blue-glow: #3f7fd0;
    --blue-light: #6fb0ee;
    --white: #ffffff;
    --ink: #141414;
    --gold: #e2ad3a;
    --gold-light: #f3d27a;
  }
  * { margin: 0; padding: 0; box-sizing: border-box; }
  html, body { width: 1200px; height: 1200px; overflow: hidden; }
  body {
    background: var(--page);
    font-family: "Open Sans", Arial, sans-serif;
    color: var(--white);
    position: relative;
  }
  .card {
    position: absolute;
    width: 819px;
    height: 470px;
    overflow: hidden;
    background: linear-gradient(120deg, var(--navy-deep) 0%, var(--navy) 55%, #234a86 100%);
    box-shadow: 0 6px 14px rgba(0,0,0,0.25);
  }
  .card--front { left: 129px; top: 94px; }
  .card--back { left: 282px; top: 623px; }

  .network-art {
    position: absolute;
    inset: 0;
    background: radial-gradient(ellipse 60% 75% at 100% 100%, var(--blue-light) 0%, var(--blue-glow) 30%, rgba(40,80,150,0.45) 60%, rgba(26,45,85,0) 85%);
  }
  .arc { position: absolute; inset: 0; }

  .name-band {
    position: absolute;
    left: 0; top: 59px;
    width: 430px; height: 70px;
    background: var(--white);
    border-radius: 0 35px 35px 0;
    display: flex; align-items: center;
    padding-left: 60px;
  }
  .name-band h1 {
    font-family: "Montserrat", Arial, sans-serif;
    font-weight: 700;
    font-size: 31px;
    letter-spacing: 2.5px;
    color: var(--ink);
    text-transform: uppercase;
  }

  .contact-list { position: absolute; left: 71px; top: 188px; list-style: none; }
  .contact-item { display: flex; align-items: center; height: 38px; margin-bottom: 11px; }
  .contact-icon {
    width: 38px; height: 38px; border-radius: 50%;
    background: var(--white);
    display: flex; align-items: center; justify-content: center;
    flex-shrink: 0;
  }
  .contact-text { margin-left: 18px; font-size: 18px; line-height: 23px; font-weight: 400; }
  .contact-text--email { font-size: 21px; margin-left: 18px; }

  .pager { position: absolute; left: 98px; top: 425px; display: flex; gap: 13px; }
  .pager span { width: 20px; height: 20px; border-radius: 50%; background: var(--white); }

  .brand { position: absolute; text-align: center; color: var(--gold); font-family: "Open Sans", Arial, sans-serif; }
  .brand__name { font-weight: 600; letter-spacing: 6px; line-height: 1; }
  .brand__tagline { font-weight: 600; letter-spacing: 0.5px; margin-top: 8px; }
  .card--front .brand { left: 560px; top: 190px; width: 220px; }
  .card--front .brand__name { font-size: 40px; }
  .card--front .brand__tagline { font-size: 17px; }
  .card--back .brand { left: 590px; top: 350px; width: 210px; }
  .card--back .brand__name { font-size: 46px; }
  .card--back .brand__tagline { font-size: 22px; }

  .services { position: absolute; left: 57px; top: 118px; letter-spacing: 1.6px; font-size: 18px; font-weight: 600; }
  .services__intro { margin-left: 22px; margin-bottom: 22px; }
  .services__list { list-style: none; }
  .services__list li { position: relative; padding-left: 22px; line-height: 23.6px; }
  .services__list li::before {
    content: ""; position: absolute; left: 0; top: 8px;
    width: 8px; height: 8px; border-radius: 50%; background: var(--white);
  }
</style>
</head>
<body>

<section class="card card--front">
  <div class="network-art" role="img" aria-label="Glowing blue network of connected nodes and lines"></div>
  <svg class="arc" width="819" height="470" viewBox="0 0 819 470" aria-hidden="true">
    <circle cx="800" cy="490" r="228" fill="none" stroke="rgba(255,255,255,0.35)" stroke-width="6"/>
  </svg>

  <div class="name-band"><h1>Derek Halloran</h1></div>

  <ul class="contact-list">
    <li class="contact-item">
      <span class="contact-icon">
        <svg width="22" height="16" viewBox="0 0 22 16"><rect x="1" y="1" width="20" height="14" fill="none" stroke="#222" stroke-width="1.4"/><path d="M1 1 L11 9 L21 1 M1 15 L8 7 M21 15 L14 7" fill="none" stroke="#222" stroke-width="1.4"/></svg>
      </span>
      <span class="contact-text contact-text--email">DHalloran@VELTRAsmarthomes.com</span>
    </li>
    <li class="contact-item">
      <span class="contact-icon">
        <svg width="22" height="22" viewBox="0 0 22 22" fill="none" stroke="#222" stroke-width="1.2"><circle cx="11" cy="11" r="9.5"/><ellipse cx="11" cy="11" rx="4.5" ry="9.5"/><path d="M1.5 11 H20.5 M3 6 H19 M3 16 H19 M11 1.5 V20.5"/></svg>
      </span>
      <span class="contact-text">www.veltrasmarthomes.com</span>
    </li>
    <li class="contact-item">
      <span class="contact-icon">
        <svg width="22" height="22" viewBox="0 0 24 24"><path d="M6.6 10.8c1.4 2.8 3.8 5.1 6.6 6.6l2.2-2.2c.3-.3.7-.4 1-.2 1.1.4 2.3.6 3.6.6.6 0 1 .4 1 1V20c0 .6-.4 1-1 1C10.6 21 3 13.4 3 4c0-.6.4-1 1-1h3.5c.6 0 1 .4 1 1 0 1.3.2 2.5.6 3.6.1.3 0 .7-.2 1z" fill="#222"/></svg>
      </span>
      <span class="contact-text">+34-602-518-794</span>
    </li>
    <li class="contact-item">
      <span class="contact-icon">
        <svg width="18" height="24" viewBox="0 0 18 24"><path d="M9 1C4.6 1 1 4.5 1 8.9 1 14.8 9 23 9 23s8-8.2 8-14.1C17 4.5 13.4 1 9 1z" fill="#222"/><circle cx="9" cy="9" r="3" fill="#fff"/></svg>
      </span>
      <span class="contact-text">Plaza Brisa Local 42,<br>Port Andratx, 07392</span>
    </li>
  </ul>

  <div class="pager" aria-hidden="true"><span></span><span></span><span></span></div>

  <div class="brand">
    <div class="brand__name">VELTRA</div>
    <div class="brand__tagline">Smarter Homes</div>
  </div>
</section>

<section class="card card--back">
  <div class="network-art" role="img" aria-label="Glowing blue network of connected nodes and lines"></div>
  <svg class="arc" width="819" height="472" viewBox="0 0 819 472" aria-hidden="true">
    <defs>
      <linearGradient id="goldArc" x1="0" y1="1" x2="1" y2="0">
        <stop offset="0" stop-color="#d9a22c"/>
        <stop offset="0.6" stop-color="#f3d27a"/>
        <stop offset="1" stop-color="#e2ad3a"/>
      </linearGradient>
    </defs>
    <circle cx="830" cy="480" r="368" fill="none" stroke="url(#goldArc)" stroke-width="16"/>
  </svg>

  <div class="services">
    <p class="services__intro">Design, sales, installation, and maintenance of</p>
    <ul class="services__list">
      <li>Home Automation systems</li>
      <li>Distributed / Multi-Room Audio and Video</li>
      <li>High Performance Networks &amp; WiFi</li>
      <li>Lighting and Shade Control</li>
      <li>Home cinema</li>
      <li>Security and CCTV Systems</li>
    </ul>
  </div>

  <div class="brand">
    <div class="brand__name">VELTRA</div>
    <div class="brand__tagline">Smarter Homes</div>
  </div>
</section>

</body>
</html>
```